Tri-fold brochue, business card, and stationary design.

Tri-fold brochure: We are looking to get a tri-fold brochure template created so we can add our content on each side of the brochure and then leave these with prospective clients during sales calls.Business card: We would like the business card to have employee name, phone number, and email address on the card. We are open to rounded corners as well.We just redid our website and we'd like all designs to be complementary to our new "Look and feel" of our website.

Contact Information for Business Card

We would like the business card to have employee name, phone number, and email address on the card. We are open to rounded corners as well.

We just redid our website and we'd like all designs to be complementary to our new "Look and feel" of our website.

```html
<!DOCTYPE html>
<html lang="en">
<head>
<meta charset="utf-8">
<title>Tidewater Systems – Tri-fold Brochure</title>
<link href="https://fonts.googleapis.com/css2?family=Montserrat:wght@400;600;700;800&family=Open+Sans:wght@400;600&display=swap" rel="stylesheet">
<style>
  :root{
    --blue:#1c92d8;
    --blue-deep:#136fb0;
    --navy:#1d3553;
    --charcoal:#2c3038;
    --grey:#e6e9ec;
    --grey-mid:#c9ced4;
    --text:#5b6470;
    --white:#ffffff;
    --photo-a:#2d5f8e;
    --photo-b:#9bb8cf;
    --stage:#eef0f2;
  }
  *{box-sizing:border-box;margin:0;padding:0}
  html,body{width:872px;height:1200px;overflow:hidden;background:var(--stage)}
  body{position:relative;font-family:"Open Sans",Arial,sans-serif;color:var(--text)}
  .spread{position:absolute;left:46px;width:780px;display:flex;box-shadow:0 8px 24px rgba(0,0,0,.18);background:var(--white)}
  .spread--outside{top:36px;height:500px}
  .spread--inside{top:596px;height:560px}
  .panel{position:relative;width:260px;height:100%;overflow:hidden}
  .panel + .panel{border-left:1px solid #dfe3e7}
  .panel svg.bg{position:absolute;inset:0;width:100%;height:100%}
  .abs{position:absolute}
  .heading{font-family:"Montserrat",Arial,sans-serif;font-weight:800}
  .whatif-title{font-size:24px;color:var(--white)}
  .whatif-list{list-style:none}
  .whatif-list li{display:flex;gap:8px;align-items:flex-start;font-size:8.5px;line-height:1.35;color:var(--white);margin-bottom:9px}
  .whatif-list .dot{flex:0 0 16px;height:16px;border-radius:50%;background:var(--white);position:relative}
  .whatif-list .dot::after{content:"";position:absolute;left:5px;top:3px;width:4px;height:7px;border:solid var(--blue);border-width:0 2px 2px 0;transform:rotate(45deg)}
  .brand{font-family:"Montserrat",Arial,sans-serif;font-weight:700;color:var(--blue);display:flex;align-items:center;gap:8px}
  .brand .mark{width:14px;height:14px;border-radius:50%;background:var(--blue)}
  .contact{font-size:8px;line-height:1.5;color:var(--text)}
  .contact p{display:flex;gap:6px;align-items:center;margin-bottom:3px}
  .contact svg{width:9px;height:9px;flex:0 0 9px}
  .reasons-title{font-family:"Montserrat",Arial,sans-serif;font-weight:800;color:var(--blue);font-size:17px;line-height:1.1}
  .reasons-sub{font-family:"Montserrat",Arial,sans-serif;font-weight:600;color:var(--charcoal);font-size:10px;margin-top:2px}
  .reasons-list{list-style:none;margin-top:12px}
  .reasons-list li{font-size:8.5px;line-height:1.3;color:var(--text);padding-left:12px;position:relative;margin-bottom:6px}
  .reasons-list li::before{content:"";position:absolute;left:0;top:3px;width:5px;height:5px;background:var(--blue)}
  .badge-num{background:var(--blue);color:var(--white);font-family:"Montserrat",Arial,sans-serif;font-weight:700;font-size:18px;padding:6px 10px}
  .tagline{font-family:"Montserrat",Arial,sans-serif;font-weight:700;color:var(--blue);font-size:13px;line-height:1.25}
  .phone{font-family:"Montserrat",Arial,sans-serif;font-weight:600;font-size:9px;color:var(--charcoal);display:flex;align-items:center;gap:5px}
  .about{font-size:8.5px;line-height:1.5;color:var(--text)}
  .about p + p{margin-top:8px}
  .whatif-boxes{list-style:none}
  .whatif-boxes li{border:1px solid rgba(255,255,255,.85);border-radius:14px;padding:6px 10px 6px 32px;font-size:8.5px;line-height:1.3;color:var(--white);margin-bottom:8px;position:relative}
  .whatif-boxes li::before{content:"";position:absolute;left:8px;top:50%;width:16px;height:16px;margin-top:-8px;border-radius:50%;background:var(--white)}
</style>
</head>
<body>

<!-- Outside spread -->
<section class="spread spread--outside">

  <div class="panel panel--inner-flap">
    <svg class="bg" viewBox="0 0 260 500" preserveAspectRatio="none">
      <rect width="260" height="500" fill="#ffffff"/>
      <polygon points="0,0 260,0 260,250 0,300" fill="var(--blue)"/>
      <polygon points="0,0 70,0 0,90" fill="var(--blue-deep)"/>
      <polygon points="150,300 260,250 260,360" fill="var(--charcoal)"/>
      <polygon points="0,300 150,272 70,420" fill="var(--grey)"/>
      <rect x="0" y="430" width="260" height="70" fill="var(--grey)"/>
    </svg>
    <h2 class="abs heading whatif-title" style="left:22px;top:26px">What if...</h2>
    <ul class="abs whatif-list" style="left:22px;top:70px;width:215px">
      <li><span class="dot"></span>I could add one more IT expert to my team without the hiring cost.</li>
      <li><span class="dot"></span>I had a partner that knew my systems and fixed issues before they began.</li>
      <li><span class="dot"></span>I could get clear reports on every ticket, update and project.</li>
      <li><span class="dot"></span>My staff could call one number and get help in minutes.</li>
    </ul>
  </div>

  <div class="panel panel--back">
    <svg class="bg" viewBox="0 0 260 500" preserveAspectRatio="none">
      <rect width="260" height="500" fill="#ffffff"/>
      <defs>
        <linearGradient id="photoBack" x1="0" y1="0" x2="1" y2="1">
          <stop offset="0" stop-color="var(--photo-b)"/>
          <stop offset="1" stop-color="var(--photo-a)"/>
        </linearGradient>
      </defs>
      <polygon points="30,140 230,140 130,280" fill="url(#photoBack)" role="img" aria-label="Photo of a technician working on a laptop"/>
      <polygon points="0,140 30,140 0,200" fill="var(--blue)"/>
      <polygon points="230,140 260,140 260,220" fill="var(--charcoal)"/>
      <rect x="0" y="470" width="260" height="30" fill="var(--grey)"/>
    </svg>
    <div class="abs brand" style="left:58px;top:30px;font-size:14px"><span class="mark"></span>Tidewater Systems</div>
    <div class="abs contact" style="left:58px;top:62px">
      <p><svg viewBox="0 0 10 10"><path d="M5 0C3 0 1.5 1.5 1.5 3.5 1.5 6 5 10 5 10s3.5-4 3.5-6.5C8.5 1.5 7 0 5 0z" fill="var(--blue)"/></svg>40 Harbor Lane, Suite 200, Portland</p>
      <p><svg viewBox="0 0 10 10"><path d="M2 0l2 2-1 1.5c.8 1.6 1.9 2.7 3.5 3.5L8 6l2 2-1.5 2C4 10 0 6 0 1.5z" fill="var(--blue)"/></svg>(555) 018-2470</p>
      <p><svg viewBox="0 0 10 10"><rect x="0" y="2" width="10" height="6" fill="var(--blue)"/><path d="M0 2l5 3.5L10 2" stroke="#fff" fill="none"/></svg>hello@tidewatersys.com</p>
    </div>
    <div class="abs" style="left:24px;top:300px;width:215px">
      <h2 class="reasons-title">Top Reasons</h2>
      <p class="reasons-sub">to Call Tidewater Now!</p>
      <ul class="reasons-list">
        <li>Need a new IT support partner</li>
        <li>Struggling to keep up with network demands</li>
        <li>Need to update your IT security plan</li>
        <li>Moving to a new office</li>
        <li>Need help with cloud and email</li>
        <li>Want a fixed monthly IT budget</li>
      </ul>
    </div>
  </div>

  <div class="panel panel--cover">
    <svg class="bg" viewBox="0 0 260 500" preserveAspectRatio="none">
      <defs>
        <linearGradient id="photoCover" x1="0" y1="0" x2="1" y2="1">
          <stop offset="0" stop-color="var(--photo-a)"/>
          <stop offset="1" stop-color="var(--navy)"/>
        </linearGradient>
      </defs>
      <rect width="260" height="500" fill="#ffffff"/>
      <polygon points="0,0 260,0 260,250 130,310 0,250" fill="url(#photoCover)" role="img" aria-label="Photo of a hand using a smartphone"/>
      <polygon points="0,0 120,0 0,130" fill="var(--blue)" opacity=".9"/>
      <polygon points="0,250 130,310 0,330" fill="var(--blue)"/>
      <polygon points="260,250 130,310 260,340" fill="var(--charcoal)"/>
      <rect x="0" y="470" width="260" height="30" fill="var(--grey)"/>
    </svg>
    <div class="abs badge-num" style="right:22px;top:150px">01</div>
    <p class="abs tagline" style="left:22px;top:360px;width:130px">IT Support Giving you the Blues?</p>
    <div class="abs brand" style="left:165px;top:362px;font-size:9px;flex-direction:column;gap:4px;align-items:center;text-align:center"><span class="mark" style="width:18px;height:18px"></span>Tidewater<br>Systems</div>
    <div class="abs phone" style="right:22px;top:430px"><svg width="9" height="9" viewBox="0 0 10 10"><path d="M2 0l2 2-1 1.5c.8 1.6 1.9 2.7 3.5 3.5L8 6l2 2-1.5 2C4 10 0 6 0 1.5z" fill="var(--blue)"/></svg>(555) 018-2470</div>
  </div>
</section>

<!-- Inside spread -->
<section class="spread spread--inside">

  <div class="panel panel--intro">
    <svg class="bg" viewBox="0 0 260 560" preserveAspectRatio="none">
      <rect width="260" height="560" fill="var(--grey)"/>
      <polygon points="0,0 260,0 260,60 0,110" fill="#f4f6f8"/>
      <polygon points="200,300 260,270 260,380" fill="var(--blue)"/>
      <polygon points="0,330 260,300 260,560 0,560" fill="#dde1e5"/>
    </svg>
    <div class="abs brand" style="left:0;width:260px;top:150px;justify-content:center;font-size:22px"><span class="mark" style="width:22px;height:22px"></span>Tidewater</div>
    <div class="abs brand" style="left:0;width:260px;top:180px;justify-content:center;font-size:11px;letter-spacing:3px;color:var(--navy)">SYSTEMS</div>
    <div class="abs about" style="left:24px;top:400px;width:212px">
      <p>Tidewater Systems is a managed IT provider serving small and mid-size businesses across the region. We plan, build and support the networks our clients rely on every day.</p>
      <p>Our certified team works as an extension of your staff, keeping your systems secure, current and running so you can focus on growing your business.</p>
    </div>
  </div>

  <div class="panel panel--whatif">
    <svg class="bg" viewBox="0 0 260 560" preserveAspectRatio="none">
      <defs>
        <linearGradient id="photoInside" x1="0" y1="0" x2="1" y2="1">
          <stop offset="0" stop-color="var(--photo-b)"/>
          <stop offset="1" stop-color="var(--photo-a)"/>
        </linearGradient>
      </defs>
      <rect width="260" height="560" fill="#ffffff"/>
      <rect x="0" y="200" width="260" height="360" fill="var(--blue)"/>
      <polygon points="0,0 260,0 260,140 130,230 0,140" fill="url(#photoInside)" role="img" aria-label="Photo of a businessman touching a glowing network interface"/>
      <polygon points="0,140 130,230 0,230" fill="var(--charcoal)"/>
      <polygon points="0,0 60,0 0,70" fill="var(--blue)"/>
    </svg>
    <h2 class="abs heading whatif-title" style="left:22px;top:240px">What if...</h2>
    <ul class="abs whatif-boxes" style="left:20px;top:285px;width:220px">
      <li>I could add one more IT expert to my team without the hiring cost.</li>
      <li>I had a partner that knew my systems and fixed issues before they began.</li>
      <li>I could get clear reports on every ticket, update and project.</li>
      <li>My staff could call one number and get help in minutes.</li>
      <li>I never had to worry about backups or security again.</li>
    </ul>
  </div>

  <div class="panel panel--reasons">
    <svg class="bg" viewBox="0 0 260 560" preserveAspectRatio="none">
      <rect width="260" height="560" fill="#ffffff"/>
      <polygon points="0,0 90,0 0,120" fill="var(--blue)"/>
      <rect x="0" y="0" width="8" height="560" fill="var(--blue)"/>
      <polygon points="260,470 260,560 160,560" fill="var(--grey-mid)"/>
    </svg>
    <div class="abs" style="left:34px;top:150px;width:200px">
      <h2 class="reasons-title">Top Reasons</h2>
      <p class="reasons-sub">to Call Tidewater Now!</p>
      <ul class="reasons-list">
        <li>Need a new IT support partner</li>
        <li>Struggling to keep up with network demands</li>
        <li>Need to update your IT security plan</li>
        <li>Moving to a new office</li>
        <li>Need help with cloud and email</li>
        <li>Want a fixed monthly IT budget</li>
        <li>Looking to plan your next upgrade</li>
        <li>Tired of waiting for a call back</li>
      </ul>
    </div>
  </div>
</section>

</body>
</html>
```